Letterhead design for business

Looking for an attractive and professional letterhead that uses the logo that is attached below.

Target Market(s)

Potential bankruptcy clients.

Industry/Entity Type

Legal

Colors

Designer to choose colors to be used in the design.

Requirements
Must have
• Address for locations, phone number, and website address.
• Addresses are on website ferncoveadvice.example. Use following phone number (for tracking purposes): 555-013-8274

```html
<!DOCTYPE html>
<html lang="en">
<head>
<meta charset="utf-8">
<title>Ferncove Law Group Letterhead</title>
<link href="https://fonts.googleapis.com/css2?family=Roboto:wght@400;500&display=swap" rel="stylesheet">
<style>
  :root{
    --backdrop:#e4e4e2;
    --paper:#ffffff;
    --green:#7cc08c;
    --green-soft:#a9d8b3;
    --ink:#3c3c3c;
    --text:#6f6f6f;
    --band:#3a3a3a;
  }
  *{margin:0;padding:0;box-sizing:border-box}
  html,body{width:1200px;height:946px;overflow:hidden;background:var(--backdrop);font-family:'Roboto',sans-serif}
  .letterhead{position:absolute;left:272px;top:13px;width:655px;height:920px;background:var(--paper);box-shadow:0 4px 14px rgba(0,0,0,.18);color:var(--text)}
  .brand{position:absolute;left:53px;top:62px;display:flex;align-items:center;gap:14px}
  .brand-mark{width:44px;height:44px;background:var(--green)}
  .brand-name{font-size:25px;font-weight:400;color:var(--ink);line-height:1}
  .brand-byline{position:absolute;left:111px;top:120px;font-size:9px;color:var(--green)}
  .contact{position:absolute;left:478px;top:64px;font-size:10.5px;line-height:15px;color:var(--ink)}
  .contact .row{display:flex;align-items:center;gap:5px}
  .contact svg{width:9px;height:9px;fill:var(--green)}
  .contact .gap{margin-top:5px}
  .recipient{position:absolute;left:58px;top:267px;font-size:11.5px;line-height:17px}
  .body{position:absolute;left:58px;top:370px;width:543px;font-size:11.3px;line-height:17px;text-align:justify}
  .body p+p{margin-top:34px}
  .signature{position:absolute;left:58px;top:615px;width:128px;height:84px;background:linear-gradient(135deg,#eef7f0,#d8eedd)}
  .sign-title{position:absolute;left:58px;top:714px;font-size:11.5px}
  .footer{position:absolute;left:0;bottom:0;width:655px;height:34px}
  .footer-url{position:absolute;right:52px;bottom:12px;font-size:10px;color:#fff}
</style>
</head>
<body>
<main class="letterhead">
  <header>
    <div class="brand">
      <div class="brand-mark"></div>
      <div class="brand-name">Ferncove Law Group</div>
    </div>
    <div class="brand-byline">by Attorney M. Lindqvist</div>
    <address class="contact" style="font-style:normal">
      <div>Level 2, 17 Harbour Lane</div>
      <div>Northgate, VIC 3999</div>
      <div class="row gap"><svg viewBox="0 0 10 10"><path d="M2 0.5 3.8 2.6 2.9 3.6C3.6 5 5 6.4 6.4 7.1L7.4 6.2 9.5 8 8.3 9.5C4.5 9.2.8 5.5.5 1.7Z"/></svg>555-013-8274</div>
      <div class="row"><svg viewBox="0 0 10 10"><path d="M0 2h10v1L5 6 0 3ZM0 4l5 3 5-3v4H0Z"/></svg>info@ferncoveadvice.example</div>
    </address>
  </header>

  <div class="recipient">
    <div>Dear Hallworth</div>
    <div>Orbel Print Works Corporation</div>
    <div>Department Design</div>
  </div>

  <section class="body">
    <p>Lorem ipsum dolor sit amet, consectetuer adipiscing elit. Aenean commodo ligula eget dolor. Aenean massa. Cum sociis natoque penatibus et magnis dis parturient montes, nascetur ridiculus mus. Donec quam felis, ultricies nec, pellentesque eu, pretium quis, sem. Nulla consequat massa quis enim. Donec pede justo, fringilla vel, aliquet nec, vulputate eget, arcu. In enim justo, rhoncus ut, imperdiet a, venenatis vitae, justo. Nullam dictum felis eu pede mollis pretium. Integer tincidunt. Cras dapibus. Vivamus elementum semper nisi.Nullam dictum felis eu pede mollis pretium. Integer tincidunt. Cras dapibus. Vivamus elementum semper nisi.felis eu pede mollis pretium. Integer tincidunt. Cras dapibus.</p>
    <p>Quisque rutrum. Aenean imperdiet. Etiam ultricies nisi vel augue. Curabitur ullamcorper ultricies nisi. Nam eget dui. Etiam rhoncus. Maecenas tempus, tellus eget condimentum rhoncus, sem quam semper libero, sit amet adipiscing sem neque sed ipsum.felis pede mollis pretium. I am tincidunt. Cras dapibus.</p>
  </section>

  <div class="signature" role="img" aria-label="Handwritten signature"></div>
  <div class="sign-title">Director/Excecutive Director</div>

  <footer class="footer">
    <svg width="655" height="34" viewBox="0 0 655 34">
      <rect x="0" y="6" width="448" height="5" fill="var(--green)"/>
      <path d="M0 18H445C462 18 462 2 482 2H655V34H0Z" fill="var(--band)"/>
      <path d="M0 13H446C462 13 460 0 480 0" stroke="#ffffff" stroke-width="2" fill="none"/>
    </svg>
    <div class="footer-url">www.ferncoveadvice.example</div>
  </footer>
</main>
</body>
</html>
```